Sunbirds Postcard .psd

Please supply a print-ready layered .psd file
- 148mm wide x 105mm deep with 3mm bleed
- CMYK for gloss card

Target Market(s)

Women 25 - 40

Requirements
Must have
• Fun look - heart (casually drawn) - writing (sketch look/feel) in the background and faded to say "Love is patient and kind. Love is not jealous or boastful or proud or rude. It does not demand its own way. It is not irritable, and it keeps no record of being wronged. It does not rejoice about injustice but rejoices whenever the truth wins out. Love never gives up, never loses faith, is always hopeful, and endures through every circumstance."

images/text overlay for the front in bold colour (almost like being branded / tattooed / stamp / seal)

Text:
Front: Chosen and marked by Love (emphasise love)
Sunbirds logo (attached - use in any colour)

Back: Save the dates: 6 March, 29 May, 14 August, 27 November
Cost: $10 each event
Time: 7:00pm
Location: The Marlow, 412 Brindle St, Newcastle 2300
These events are hosted by Chapel247 to enable women across the region to inspire and encourage others to make a difference in their relationships and world. Our heart is that we as women develop a deep abiding peace, acceptance and experience the overwhelming embracing love of God.
Chapel247 Logo (attached)
Nice to have
• pictures of Women having fun / laughing (can get from PixVault - please use low res version until approved and then I will purchase).

See examples given of type (type.jpg) and background text (text.jpg)
Should not have
• not women posing for pictures, smiling at the camera

```html
<!DOCTYPE html>
<html lang="en">
<head>
<meta charset="utf-8">
<title>Sunbirds Postcard</title>
<link rel="stylesheet" href="https://fonts.googleapis.com/css2?family=Architects+Daughter&family=Rye&family=Pacifico&family=Sniglet&family=Short+Stack&display=swap">
<style>
  :root {
    --paper: #e8e6c6;
    --paper-shade: #dcdab6;
    --ink: #27284a;
    --coral: rgba(232, 132, 108, 0.78);
    --coral-light: rgba(232, 132, 108, 0.55);
    --gap: #ffffff;
  }
  * { margin: 0; padding: 0; box-sizing: border-box; }
  html, body { width: 839px; height: 1200px; overflow: hidden; background: var(--gap); }
  .canvas { position: relative; width: 839px; height: 1200px; }

  .card {
    position: absolute; left: 0; width: 839px; overflow: hidden;
    background: radial-gradient(ellipse at 50% 40%, var(--paper) 55%, var(--paper-shade) 100%);
  }
  .card--front { top: 0; height: 592px; }
  .card--back { top: 604px; height: 596px; }

  .art-area { position: absolute; border-radius: 46% 46% 50% 50%; }

  /* Front */
  .art-area--main {
    left: 214px; top: 50px; width: 340px; height: 350px;
    background: linear-gradient(160deg, var(--coral) 0%, var(--coral-light) 100%);
  }
  .verse {
    position: absolute; left: 90px; top: 66px; width: 660px;
    font-family: "Architects Daughter", cursive;
    font-size: 22px; line-height: 34px; text-transform: uppercase;
    color: var(--ink); text-align: center;
    transform: rotate(-8deg); transform-origin: center;
  }
  .title { margin: 0; font-weight: normal; }
  .title span { position: absolute; color: var(--ink); line-height: 1; white-space: nowrap; }
  .title__chosen { left: 162px; top: 380px; font-family: "Rye", serif; font-size: 54px; }
  .title__marked { left: 318px; top: 440px; font-family: "Pacifico", cursive; font-size: 26px; transform: rotate(-16deg); }
  .title__by { left: 446px; top: 478px; font-family: "Pacifico", cursive; font-size: 28px; transform: rotate(-12deg); }
  .title__love { left: 500px; top: 416px; font-family: "Rye", serif; font-size: 96px; }
  .brand {
    position: absolute; left: 668px; top: 536px;
    font-family: "Short Stack", cursive; font-size: 22px; color: var(--ink);
  }

  /* Back */
  .label { font-family: "Sniglet", sans-serif; font-weight: 400; color: var(--ink); }
  .value { font-family: "Architects Daughter", cursive; font-size: 20px; text-transform: uppercase; color: var(--ink); }
  .dates { position: absolute; left: 58px; top: 48px; white-space: nowrap; }
  .dates .label { font-size: 36px; }

  .art-area--left { left: 170px; top: 292px; width: 130px; height: 140px; background: var(--coral-light); }
  .art-area--middle { left: 362px; top: 222px; width: 118px; height: 126px; background: var(--coral-light); }
  .art-area--right { left: 548px; top: 144px; width: 122px; height: 134px; background: var(--coral-light); }

  .about {
    position: absolute; left: 60px; top: 156px; width: 720px;
    font-family: "Architects Daughter", cursive; font-size: 22px; line-height: 34px;
    text-transform: uppercase; text-align: center; color: var(--ink);
  }
  .details { position: absolute; left: 0; width: 839px; text-align: center; white-space: nowrap; line-height: 1; }
  .details--cost { top: 462px; }
  .details--location { top: 508px; }
  .details--cost .label { font-size: 38px; }
  .details--location .label { font-size: 44px; }
  .details .value { margin-right: 12px; font-size: 21px; }
</style>
</head>
<body>
<main class="canvas">
  <section class="card card--front">
    <div class="art-area art-area--main" role="img" aria-label="Casually drawn coral heart with sketched rays"></div>
    <p class="verse">Love is patient and kind. Love is not jealous or<br>boastful or proud or rude. It does not demand<br>its own way. It is not irritable, and it keeps<br>no record of being wronged. It does not rejoice<br>about injustice but rejoices whenever the<br>truth wins out. Love never gives up,<br>never loses faith, is always hopeful,<br>and endures through every circumstance.</p>
    <h1 class="title">
      <span class="title__chosen">CHOSEN</span>
      <span class="title__marked">and marked</span>
      <span class="title__by">by</span>
      <span class="title__love">LoVe</span>
    </h1>
    <div class="brand">sunbirds</div>
  </section>

  <section class="card card--back">
    <p class="dates"><span class="label">save the dates:</span> <span class="value">6 March, 29 May, 14 August, 27 November</span></p>
    <div class="art-area art-area--left" role="img" aria-label="Small sketched coral heart"></div>
    <div class="art-area art-area--middle" role="img" aria-label="Small sketched coral heart"></div>
    <div class="art-area art-area--right" role="img" aria-label="Small sketched coral heart"></div>
    <p class="about">These events are hosted by Chapel247<br>to enable women across the region to inspire<br>and encourage others to make a difference<br>in their relationships and world. Our heart is<br>that we as women develop a deep abiding peace,<br>acceptance and experience the overwhelming<br>embracing love of God.</p>
    <p class="details details--cost"><span class="label">cost:</span> <span class="value">$10 each event</span><span class="label">time:</span> <span class="value">7:00pm</span></p>
    <p class="details details--location"><span class="label">location:</span> <span class="value">The Marlow, 412 Brindle St, Newcastle 2300</span></p>
  </section>
</main>
</body>
</html>
```